MS word document templates for consultancy

I need the following templates for my business using my logo as branding.

- General report template
- Letter head template
- Tender proposal template

The templates should be sleek and with minimal colors, but with a small amount of green and grey where appropriate (as per attached logo and email signature). Font should be consistent with the text in the email signature.

```html
<!DOCTYPE html>
<html lang="en">
<head>
<meta charset="UTF-8">
<title>General Report Cover – Northpath Group</title>
<link href="https://fonts.googleapis.com/css2?family=Arimo:wght@400;700&display=swap" rel="stylesheet">
<style>
  :root {
    --green: #2a8f3e;
    --grey-band: #5c5c5c;
    --grey-text: #5a5a5a;
    --ink: #111111;
    --paper: #ffffff;
  }
  * { margin: 0; padding: 0; box-sizing: border-box; }
  html, body {
    width: 775px;
    height: 1200px;
    overflow: hidden;
    background: var(--paper);
    font-family: "Arimo", Arial, sans-serif;
  }
  .cover {
    position: relative;
    width: 775px;
    height: 1200px;
    background: var(--paper);
  }
  .edge-band {
    position: absolute;
    left: 0;
    width: 775px;
    height: 14px;
  }
  .edge-band--top { top: 18px; background: var(--grey-band); }
  .edge-band--bottom { top: 1168px; background: var(--green); }

  .brand {
    position: absolute;
    left: 46px;
    top: 78px;
    display: flex;
    align-items: center;
    gap: 12px;
  }
  .brand__name {
    font-size: 50px;
    font-weight: 400;
    color: var(--ink);
    letter-spacing: 0.5px;
    line-height: 1.1;
  }
  .brand__mark {
    width: 12px;
    height: 12px;
    background: var(--green);
    flex: none;
    margin-top: 14px;
  }
  .report-year {
    position: absolute;
    right: 62px;
    top: 84px;
    font-size: 38px;
    font-weight: 700;
    color: var(--green);
    line-height: 1.1;
  }
  .report-title {
    position: absolute;
    right: 62px;
    top: 720px;
    text-align: right;
  }
  .report-title__kicker {
    display: block;
    font-size: 43px;
    font-weight: 400;
    color: var(--grey-text);
    letter-spacing: 1px;
    line-height: 1;
  }
  .report-title__main {
    display: block;
    font-size: 80px;
    font-weight: 700;
    color: var(--green);
    line-height: 1;
    margin-top: 10px;
  }
  .title-rule {
    position: absolute;
    left: 351px;
    top: 886px;
    width: 362px;
    height: 3px;
    background: var(--green);
  }
  .contact {
    position: absolute;
    right: 62px;
    text-align: right;
    font-size: 16px;
    line-height: 24px;
  }
  .contact--primary { top: 968px; color: var(--green); }
  .contact--web { top: 1058px; color: var(--grey-text); }
  .contact__line {
    display: flex;
    justify-content: flex-end;
    align-items: center;
    gap: 8px;
  }
  .contact__icon { width: 11px; height: 11px; flex: none; }
</style>
</head>
<body>
<main class="cover">
  <div class="edge-band edge-band--top" role="img" aria-label="Grey decorative arrow band along the top edge"></div>

  <div class="brand">
    <span class="brand__name">Northpath Group</span>
    <span class="brand__mark" aria-hidden="true"></span>
  </div>
  <div class="report-year">2025</div>

  <h1 class="report-title">
    <span class="report-title__kicker">GENERAL</span>
    <span class="report-title__main">REPORT</span>
  </h1>
  <div class="title-rule"></div>

  <div class="contact contact--primary">
    <div class="contact__line">0400 555 019
      <svg class="contact__icon" viewBox="0 0 12 12" aria-hidden="true"><path d="M3 1 L5 3.5 L4 5 Q5.5 7.5 7 8 L8.5 7 L11 9 L9.5 11 Q4 10.5 1 2.5 Z" fill="#2a8f3e"/></svg>
    </div>
    <div class="contact__line">Dummy City, Dummy Country
      <svg class="contact__icon" viewBox="0 0 12 12" aria-hidden="true"><path d="M6 1 A3 3 0 0 1 9 4 C9 6.5 6 9 6 9 C6 9 3 6.5 3 4 A3 3 0 0 1 6 1 Z" fill="#2a8f3e"/><rect x="2" y="10" width="8" height="1.5" fill="#2a8f3e"/></svg>
    </div>
  </div>

  <div class="contact contact--web">
    <div class="contact__line">info@northpathgroup.com
      <svg class="contact__icon" viewBox="0 0 12 12" aria-hidden="true"><rect x="1" y="3" width="10" height="7" fill="#5a5a5a"/><polyline points="1,3 6,7 11,3" fill="none" stroke="#ffffff" stroke-width="1"/></svg>
    </div>
    <div class="contact__line">www.northpathgroup.com
      <svg class="contact__icon" viewBox="0 0 12 12" aria-hidden="true"><circle cx="6" cy="6" r="4.5" fill="#5a5a5a"/><ellipse cx="6" cy="6" rx="2" ry="4.5" fill="none" stroke="#ffffff" stroke-width="0.8"/><line x1="1.5" y1="6" x2="10.5" y2="6" stroke="#ffffff" stroke-width="0.8"/></svg>
    </div>
  </div>

  <div class="edge-band edge-band--bottom" role="img" aria-label="Green decorative arrow band along the bottom edge"></div>
</main>
</body>
</html>
```